Valmin & Co Powerpoint Template

A simple powerpoint template for my business which provides management consulting services for Business Owners.

It should reflect the colours within the logo design and should work as the master template for all standard powerpoint slide layouts.

```html
<!DOCTYPE html>
<html lang="en">
<head>
<meta charset="utf-8">
<title>Valmin &amp; Co Presentation Template</title>
<link rel="stylesheet" href="https://fonts.googleapis.com/css2?family=Poppins:wght@300;400;500;600;700&display=swap">
<style>
:root{
  --orange:#e35f1e;
  --orange-pale:#f7d9c9;
  --ink:#2b2b2b;
  --grey:#555a5e;
  --text:#4a4a4a;
  --mist:#eaf4f2;
  --band:#4b4b4b;
  --night-1:#1b2024;
  --night-2:#3b4248;
  --stage:#eef0f2;
  --grid-bg:#c9c9c9;
}
*{box-sizing:border-box;margin:0;padding:0}
html,body{width:1200px;height:2336px;overflow:hidden}
body{position:relative;font-family:"Poppins",sans-serif;color:var(--ink);background:var(--grid-bg)}
.stage{position:absolute;left:0;top:0;width:1200px;height:725px;background:linear-gradient(180deg,#f3f4f6 0%,#e4e6e9 100%)}
.hero{position:absolute;left:150px;top:130px;transform:scale(1.65);transform-origin:0 0;box-shadow:0 4px 12px rgba(0,0,0,.25)}
.lockup{position:absolute;left:935px;top:88px;display:flex;flex-direction:column;gap:6px}
.lockup .name{display:flex;align-items:center;gap:12px;font-size:30px;font-weight:400;color:var(--ink)}
.lockup .dot{width:22px;height:22px;border-radius:50%;background:var(--orange)}
.lockup .tag{font-size:13px;font-weight:400;color:var(--ink);letter-spacing:.02em}

.s{position:absolute;width:382px;height:214px;overflow:hidden;background:#fff}
.photo{position:absolute;background:linear-gradient(135deg,#c9ccd0,#8f9aa3)}
.photo.night{background:linear-gradient(120deg,var(--night-1) 0%,var(--night-2) 55%,#22282d 100%)}
.photo.warm{background:linear-gradient(135deg,#d8cbbd,#8a6e58)}
.photo.chart{background:linear-gradient(135deg,#f4f6f8,#cfd8e2)}
.photo.desk{background:linear-gradient(135deg,#b7c2cc,#5e6a75)}

.brand{position:absolute;display:flex;flex-direction:column;gap:2px}
.brand .name{display:flex;align-items:center;gap:5px;font-size:9px;font-weight:400}
.brand .dot{width:8px;height:8px;border-radius:50%;background:var(--orange)}
.brand .tag{font-size:4px}
.on-dark{color:#fff}
.on-light{color:var(--ink)}

.title{position:absolute;font-size:17px;line-height:1.15;color:var(--orange)}
.title b{font-weight:700;display:block}
.title span{font-weight:400;display:block}
.sub{position:absolute;font-size:7.5px;font-weight:400}
.date{position:absolute;font-size:4.5px;letter-spacing:.2em;font-weight:500}
.bar-bottom{position:absolute;left:0;bottom:0;width:100%;height:14px;display:flex;align-items:center;justify-content:center;font-size:3.8px;font-weight:500}
.bar-bottom.mist{background:var(--mist);color:var(--ink)}
.bar-bottom.ink{background:var(--band);color:#fff}
.panel{position:absolute;background:var(--mist)}
.rule{position:absolute;height:4px;background:var(--orange)}

.hd{position:absolute;left:25px;top:14px;font-size:9.5px;font-weight:400;color:var(--ink)}
.hd b{font-weight:600}
.hd::after{content:"";position:absolute;left:0;top:17px;width:18px;height:2px;background:var(--orange)}
.foot{position:absolute;left:0;bottom:0;width:100%;height:26px}
.foot .fb{position:absolute;left:12px;top:8px;font-size:5.5px;color:var(--ink);display:flex;align-items:center;gap:3px}
.foot .fb i{width:5px;height:5px;border-radius:50%;background:var(--orange)}
.foot .fc{position:absolute;right:24px;top:10px;font-size:3.6px;font-weight:600}
.foot .pg{position:absolute;right:11px;top:9px;width:7px;height:7px;background:var(--orange);color:#fff;font-size:3.5px;display:flex;align-items:center;justify-content:center}

.t{position:absolute;font-size:4.2px;line-height:1.4;color:var(--text)}
.t p+p{margin-top:3px}
.t ul{padding-left:7px}
.t li{margin-bottom:2px}
.t li::marker{color:var(--orange)}
.oh{position:absolute;font-size:5.5px;font-weight:600;color:var(--orange)}
.oh span{font-weight:400}
.ch{position:absolute;font-size:5.5px;font-weight:600;color:var(--ink);text-align:center}
.ch.or{color:var(--orange)}

.toc{position:absolute;display:flex;gap:8px;width:150px}
.toc .n{font-size:14px;font-weight:300;color:#888;width:14px;text-align:center}
.toc .h{font-size:5.5px;font-weight:600;color:var(--orange)}
.toc .h span{font-weight:400}
.toc .d{font-size:3.8px;line-height:1.35;color:var(--text)}

.chev{position:absolute;top:59px;width:74px;height:13px;clip-path:polygon(0 0,88% 0,100% 50%,88% 100%,0 100%,12% 50%)}
.chev.or{background:var(--orange)}.chev.dk{background:var(--grey)}
.ic{position:absolute;width:18px;height:18px;border-radius:50%;border:1.5px solid #fff;display:flex;align-items:center;justify-content:center}
.ic.or{background:var(--orange)}.ic.dk{background:var(--grey)}
.ic svg{width:9px;height:9px}
.ic.lg{width:20px;height:20px;border:none}

table.grid{position:absolute;left:22px;top:50px;width:338px;border-collapse:collapse;font-size:3.6px;color:var(--text)}
table.grid th{height:14px;font-size:4.2px;font-weight:600;color:#fff;background:var(--band);text-align:center;border:.5px solid #fff}
table.grid th:first-child{background:#111;text-align:left;padding-left:3px}
table.grid th.hl{background:var(--orange)}
table.grid td{height:19px;padding:1px 3px;border-bottom:.5px solid #ccc;line-height:1.3}
table.grid td:first-child{font-size:4.6px;color:var(--ink)}
table.grid td.hl{background:var(--orange-pale)}

.contact{position:absolute;font-size:4.5px;display:flex;flex-direction:column;gap:5px}
.contact div{display:flex;align-items:center;gap:5px}
.contact i{width:5px;height:5px;border-radius:50%;border:1px solid var(--orange)}
.ct{position:absolute;font-size:7px;font-weight:600}
</style>
</head>
<body>

<section class="stage">
  <div class="s hero">
    <div class="photo night" style="inset:0" role="img" aria-label="Dim photo of two people shaking hands over a laptop"></div>
    <div class="brand on-dark" style="left:35px;top:40px"><div class="name"><i class="dot"></i>Valmin &amp; Co</div><div class="tag">Supporting Business Owners</div></div>
    <div class="title" style="left:35px;top:104px"><b>Presentation Title</b><span>Goes Here</span></div>
    <div class="sub on-dark" style="left:35px;top:146px">Subtitle of Presentation Goes Here</div>
    <div class="date on-dark" style="left:35px;top:163px">Sunday, September 3, 2023</div>
    <div class="bar-bottom mist">© Valmin &amp; Co 2023. All Rights Reserved.</div>
  </div>
  <div class="lockup">
    <div class="name"><i class="dot"></i>Valmin &amp; Co</div>
    <div class="tag">Supporting Business Owners</div>
  </div>
</section>

<!-- row 1 -->
<div class="s" style="left:15px;top:741px">
  <div class="photo night" style="inset:0" role="img" aria-label="Dim photo of two people shaking hands over a laptop"></div>
  <div class="brand on-dark" style="left:35px;top:40px"><div class="name"><i class="dot"></i>Valmin &amp; Co</div><div class="tag">Supporting Business Owners</div></div>
  <div class="title" style="left:35px;top:104px"><b>Presentation Title</b><span>Goes Here</span></div>
  <div class="sub on-dark" style="left:35px;top:146px">Subtitle of Presentation Goes Here</div>
  <div class="date on-dark" style="left:35px;top:163px">Sunday, September 3, 2023</div>
  <div class="bar-bottom mist">© Valmin &amp; Co 2023. All Rights Reserved.</div>
</div>

<div class="s" style="left:410px;top:741px">
  <div class="brand on-light" style="left:35px;top:40px"><div class="name"><i class="dot"></i>Valmin &amp; Co</div><div class="tag">Supporting Business Owners</div></div>
  <div class="title" style="left:35px;top:104px"><b>Presentation Title</b><span>Goes Here</span></div>
  <div class="sub on-light" style="left:35px;top:146px">Subtitle of Presentation Goes Here</div>
  <div class="date on-light" style="left:35px;top:163px">Sunday, September 3, 2023</div>
  <div class="bar-bottom ink">© Valmin &amp; Co 2023. All Rights Reserved.</div>
</div>

<div class="s" style="left:803px;top:741px">
  <div class="photo night" style="inset:0" role="img" aria-label="Dim photo of a business meeting"></div>
  <div class="panel" style="left:0;top:62px;width:245px;height:90px"></div>
  <div class="title" style="left:34px;top:70px"><b>Presentation Title</b><b>Goes Here</b></div>
  <div class="sub on-light" style="left:34px;top:110px">Subtitle of Presentation Goes Here</div>
  <div class="date on-light" style="left:34px;top:132px;letter-spacing:0;font-size:3.8px">Sunday, September 3, 2023</div>
  <div class="rule" style="left:34px;top:148px;width:170px"></div>
  <div class="brand on-dark" style="left:270px;top:86px"><div class="name"><i class="dot"></i>Valmin &amp; Co</div><div class="tag">Supporting Business Owners</div></div>
</div>

<!-- row 2 -->
<div class="s" style="left:15px;top:968px">
  <div class="photo night" style="inset:0" role="img" aria-label="Dim photo of a business meeting"></div>
  <div class="brand on-dark" style="left:35px;top:22px"><div class="name"><i class="dot"></i>Valmin &amp; Co</div><div class="tag">Supporting Business Owners</div></div>
  <div class="panel" style="left:0;top:82px;width:282px;height:88px"></div>
  <div class="title" style="left:34px;top:90px"><b>Presentation Title</b><b>Goes Here</b></div>
  <div class="sub on-light" style="left:34px;top:130px">Subtitle of Presentation Goes Here</div>
  <div class="date on-light" style="left:34px;top:151px;letter-spacing:0;font-size:3.8px">Sunday, September 3, 2023</div>
  <div class="rule" style="left:34px;top:166px;width:175px"></div>
</div>

<div class="s" style="left:410px;top:968px">
  <h2 class="hd">Table of <b>Contents</b></h2>
  <div class="toc" style="left:50px;top:60px"><div class="n">1</div><div><div class="h">Title <span>Goes Here</span></div><div class="d">Short note on the first topic to cover in this section.</div></div></div>
  <div class="toc" style="left:200px;top:60px"><div class="n">2</div><div><div class="h">Title <span>Goes Here</span></div><div class="d">Short note on the second topic to cover in this section.</div></div></div>
  <div class="toc" style="left:50px;top:97px"><div class="n">3</div><div><div class="h">Title <span>Goes Here</span></div><div class="d">Short note on the third topic to cover in this section.</div></div></div>
  <div class="toc" style="left:200px;top:97px"><div class="n">4</div><div><div class="h">Title <span>Goes Here</span></div><div class="d">Short note on the fourth topic to cover in this section.</div></div></div>
  <div class="toc" style="left:50px;top:134px"><div class="n">5</div><div><div class="h">Title <span>Goes Here</span></div><div class="d">Short note on the fifth topic to cover in this section.</div></div></div>
  <div class="toc" style="left:200px;top:134px"><div class="n">6</div><div><div class="h">Title <span>Goes Here</span></div><div class="d">Short note on the sixth topic to cover in this section.</div></div></div>
  <div class="foot"><span class="fb"><i></i>Valmin &amp; Co</span><span class="fc">© Valmin &amp; Co 2023. All Rights Reserved.</span><span class="pg">5</span></div>
</div>

<div class="s" style="left:803px;top:968px">
  <h2 class="hd"><b>Heading</b> Goes Here</h2>
  <div class="t" style="left:25px;top:52px;width:332px">
    <p>Clear advice helps owners plan growth, manage costs and lead their teams with confidence. We review the numbers, map the risks and set out simple steps that keep the business on track through every season of change and every new goal.</p>
    <p>Each plan starts with a frank look at where the business stands today. From there we agree priorities, assign owners and set dates so progress can be measured, shared and improved month after month with the whole team.</p>
    <p>Good reporting keeps everyone aligned. Short reviews show what is working, what needs attention and where the next opportunity lies, so decisions are made on facts rather than guesswork.</p>
  </div>
  <div class="foot"><span class="fb"><i></i>Valmin &amp; Co</span><span class="fc">© Valmin &amp; Co 2023. All Rights Reserved.</span><span class="pg">6</span></div>
</div>

<!-- row 3 -->
<div class="s" style="left:15px;top:1194px">
  <h2 class="hd"><b>Heading</b> Goes Here</h2>
  <div class="photo desk" style="left:22px;top:50px;width:162px;height:60px" role="img" aria-label="Photo of a man working on a tablet"></div>
  <div class="photo warm" style="left:198px;top:50px;width:162px;height:60px" role="img" aria-label="Photo of hands reviewing printed documents"></div>
  <div class="oh" style="left:25px;top:118px">Heading <span>Goes Here</span></div>
  <div class="oh" style="left:201px;top:118px">Heading <span>Goes Here</span></div>
  <div class="t" style="left:25px;top:128px;width:155px"><p>Clear advice helps owners plan growth, manage costs and lead teams with confidence through steady change.</p></div>
  <div class="t" style="left:201px;top:128px;width:155px"><p>Clear advice helps owners plan growth, manage costs and lead teams with confidence through steady change.</p></div>
  <div class="foot"><span class="fb"><i></i>Valmin &amp; Co</span><span class="fc">© Valmin &amp; Co 2023. All Rights Reserved.</span><span class="pg">7</span></div>
</div>

<div class="s" style="left:410px;top:1194px">
  <h2 class="hd"><b>Heading</b> Goes Here</h2>
  <div class="oh" style="left:25px;top:50px">Heading <span>Goes Here</span></div>
  <div class="oh" style="left:201px;top:50px">Heading <span>Goes Here</span></div>
  <div class="t" style="left:25px;top:60px;width:158px"><p>Clear advice helps owners plan growth, manage costs and lead teams with confidence.</p><p>Each plan starts with a frank look at where the business stands today, then sets out clear priorities and dates.</p><p>Short reviews show what works and what needs attention next.</p><p>Good reporting keeps everyone aligned on goals.</p></div>
  <div class="t" style="left:201px;top:60px;width:158px"><p>Clear advice helps owners plan growth, manage costs and lead teams with confidence.</p><p>Each plan starts with a frank look at where the business stands today, then sets out clear priorities and dates.</p><p>Short reviews show what works and what needs attention next.</p><p>Good reporting keeps everyone aligned on goals.</p></div>
  <div class="foot"><span class="fb"><i></i>Valmin &amp; Co</span><span class="fc">© Valmin &amp; Co 2023. All Rights Reserved.</span><span class="pg">8</span></div>
</div>

<div class="s" style="left:803px;top:1194px">
  <h2 class="hd" style="top:22px"><b>Heading</b> Goes Here</h2>
  <div class="photo warm" style="left:204px;top:0;width:178px;height:165px" role="img" aria-label="Photo of two people pointing at a printed report"></div>
  <div class="t" style="left:25px;top:55px;width:168px"><p>Clear advice helps owners plan growth, manage costs and lead teams with confidence. Each plan starts with a frank look at where the business stands.</p>
    <ul style="margin-top:6px"><li>Agree priorities and set clear dates.</li><li>Review the numbers every month.</li><li>Share progress with the whole team.</li><li>Act early on the risks that matter.</li><li>Plan the next step with confidence.</li></ul></div>
  <div class="foot"><span class="fb"><i></i>Valmin &amp; Co</span><span class="fc">© Valmin &amp; Co 2023. All Rights Reserved.</span><span class="pg">9</span></div>
</div>

<!-- row 4 -->
<div class="s" style="left:15px;top:1421px">
  <h2 class="hd"><b>Heading</b> Goes Here</h2>
  <div class="chev or" style="left:20px"></div><div class="chev dk" style="left:88px"></div><div class="chev or" style="left:156px"></div><div class="chev dk" style="left:224px"></div><div class="chev or" style="left:292px"></div>
  <div class="ic or" style="left:45px;top:56px"><svg viewBox="0 0 10 10"><circle cx="5" cy="4" r="3" fill="#fff"/><rect x="4" y="7" width="2" height="2" fill="#fff"/></svg></div>
  <div class="ic dk" style="left:113px;top:56px"><svg viewBox="0 0 10 10"><circle cx="3" cy="4" r="1.6" fill="#fff"/><circle cx="7" cy="4" r="1.6" fill="#fff"/><rect x="1" y="6" width="8" height="3" rx="1" fill="#fff"/></svg></div>
  <div class="ic or" style="left:181px;top:56px"><svg viewBox="0 0 10 10"><rect x="4" y="1" width="2" height="2" fill="#fff"/><rect x="1" y="6" width="2" height="2" fill="#fff"/><rect x="7" y="6" width="2" height="2" fill="#fff"/><path d="M5 3v2M2 6V5h6v1" stroke="#fff" fill="none"/></svg></div>
  <div class="ic dk" style="left:249px;top:56px"><svg viewBox="0 0 10 10"><rect x="1" y="6" width="2" height="3" fill="#fff"/><rect x="4" y="4" width="2" height="5" fill="#fff"/><rect x="7" y="2" width="2" height="7" fill="#fff"/></svg></div>
  <div class="ic or" style="left:317px;top:56px"><svg viewBox="0 0 10 10"><text x="5" y="8.5" font-size="9" font-family="Poppins,sans-serif" font-weight="700" text-anchor="middle" fill="#fff">$</text></svg></div>
  <div class="ch or" style="left:26px;top:85px;width:62px">Heading</div><div class="ch" style="left:94px;top:85px;width:62px">Heading</div><div class="ch or" style="left:162px;top:85px;width:62px">Heading</div><div class="ch" style="left:230px;top:85px;width:62px">Heading</div><div class="ch or" style="left:298px;top:85px;width:62px">Heading</div>
  <div class="t" style="left:26px;top:98px;width:62px;text-align:center">Clear advice helps owners plan growth and manage costs with care.<p>Set goals and review each month.</p></div>
  <div class="t" style="left:94px;top:98px;width:62px;text-align:center">Clear advice helps owners plan growth and manage costs with care.<p>Set goals and review each month.</p></div>
  <div class="t" style="left:162px;top:98px;width:62px;text-align:center">Clear advice helps owners plan growth and manage costs with care.<p>Set goals and review each month.</p></div>
  <div class="t" style="left:230px;top:98px;width:62px;text-align:center">Clear advice helps owners plan growth and manage costs with care.<p>Set goals and review each month.</p></div>
  <div class="t" style="left:298px;top:98px;width:62px;text-align:center">Clear advice helps owners plan growth and manage costs with care.<p>Set goals and review each month.</p></div>
  <div class="foot"><span class="fb"><i></i>Valmin &amp; Co</span><span class="fc">© Valmin &amp; Co 2023. All Rights Reserved.</span><span class="pg">10</span></div>
</div>

<div class="s" style="left:410px;top:1421px">
  <div class="photo chart" style="left:26px;top:0;width:152px;height:165px" role="img" aria-label="Photo of a hand with a pen over printed bar charts"></div>
  <h2 class="hd" style="left:194px;top:22px"><b>Heading</b> Goes Here</h2>
  <div class="t" style="left:194px;top:52px;width:165px"><p style="font-weight:600;color:var(--ink)">Clear advice helps owners plan growth, manage costs and lead teams with confidence.</p><p>Each plan starts with a frank look at where the business stands today, then sets priorities and dates.</p><p>Short reviews show what works, what needs attention and where the next chance lies.</p><p>Good reporting keeps everyone aligned, so decisions rest on facts rather than guesswork and plans stay on track.</p></div>
  <div class="foot"><span class="fb"><i></i>Valmin &amp; Co</span><span class="fc">© Valmin &amp; Co 2023. All Rights Reserved.</span><span class="pg">11</span></div>
</div>

<div class="s" style="left:803px;top:1421px">
  <h2 class="hd"><b>Heading</b> Goes Here</h2>
  <div class="ic or lg" style="left:60px;top:50px"><svg viewBox="0 0 10 10"><circle cx="5" cy="3.5" r="2" fill="#fff"/><path d="M1.5 9a3.5 3.5 0 0 1 7 0z" fill="#fff"/></svg></div>
  <div class="ic dk lg" style="left:181px;top:50px"><svg viewBox="0 0 10 10"><circle cx="5" cy="5" r="3.5" fill="none" stroke="#fff" stroke-width="1.2"/></svg></div>
  <div class="ic or lg" style="left:302px;top:50px"><svg viewBox="0 0 10 10"><path d="M2.5 1h5v3a2.5 2.5 0 0 1-5 0z" fill="#fff"/><rect x="3.5" y="8" width="3" height="1.2" fill="#fff"/></svg></div>
  <div class="ic dk lg" style="left:60px;top:115px"><svg viewBox="0 0 10 10"><rect x="1.5" y="2" width="7" height="6.5" rx=".5" fill="none" stroke="#fff"/><path d="M1.5 4h7" stroke="#fff"/></svg></div>
  <div class="ic or lg" style="left:181px;top:115px"><svg viewBox="0 0 10 10"><rect x="1.5" y="3" width="7" height="5.5" rx=".5" fill="#fff"/><rect x="3.5" y="1.5" width="3" height="1.5" fill="none" stroke="#fff"/></svg></div>
  <div class="ic dk lg" style="left:302px;top:115px"><svg viewBox="0 0 10 10"><circle cx="5" cy="5" r="3.5" fill="none" stroke="#fff" stroke-width="1.1"/><path d="M5 3v2h1.6" stroke="#fff" fill="none"/></svg></div>
  <div class="ch or" style="left:35px;top:73px;width:70px">Heading</div><div class="ch" style="left:156px;top:73px;width:70px">Heading</div><div class="ch or" style="left:277px;top:73px;width:70px">Heading</div>
  <div class="ch" style="left:35px;top:138px;width:70px">Heading</div><div class="ch or" style="left:156px;top:138px;width:70px">Heading</div><div class="ch" style="left:277px;top:138px;width:70px">Heading</div>
  <div class="t" style="left:35px;top:82px;width:70px;text-align:center">Short note on this point for the owner.</div>
  <div class="t" style="left:156px;top:82px;width:70px;text-align:center">Short note on this point for the owner.</div>
  <div class="t" style="left:277px;top:82px;width:70px;text-align:center">Short note on this point for the owner.</div>
  <div class="t" style="left:35px;top:147px;width:70px;text-align:center">Short note on this point for the owner.</div>
  <div class="t" style="left:156px;top:147px;width:70px;text-align:center">Short note on this point for the owner.</div>
  <div class="t" style="left:277px;top:147px;width:70px;text-align:center">Short note on this point for the owner.</div>
  <div class="foot"><span class="fb"><i></i>Valmin &amp; Co</span><span class="fc">© Valmin &amp; Co 2023. All Rights Reserved.</span><span class="pg">12</span></div>
</div>

<!-- row 5 -->
<div class="s" style="left:15px;top:1647px">
  <h2 class="hd"><b>Heading</b> Goes Here</h2>
  <div class="oh" style="left:25px;top:50px">Heading <span>Goes Here</span></div>
  <div class="oh" style="left:201px;top:50px">Heading <span>Goes Here</span></div>
  <div class="t" style="left:25px;top:60px;width:160px"><ul><li>Clear advice helps owners plan growth, manage costs and lead teams with care.</li><li>Agree priorities, set dates and share them with the team.</li><li>Review the numbers each month and act early on the risks that matter most.</li><li>Short reviews show what works and where the next chance lies for growth.</li></ul></div>
  <div class="t" style="left:201px;top:60px;width:160px"><ul><li>Clear advice helps owners plan growth, manage costs and lead teams with care.</li><li>Agree priorities, set dates and share them with the team.</li><li>Review the numbers each month and act early on the risks that matter most.</li><li>Short reviews show what works and where the next chance lies for growth.</li></ul></div>
  <div class="foot"><span class="fb"><i></i>Valmin &amp; Co</span><span class="fc">© Valmin &amp; Co 2023. All Rights Reserved.</span><span class="pg">13</span></div>
</div>

<div class="s" style="left:410px;top:1647px">
  <div class="photo chart" style="left:0;top:0;width:382px;height:98px" role="img" aria-label="Photo of a pen resting on printed bar charts"></div>
  <div class="ch" style="left:0;top:108px;width:382px;font-size:9px;font-weight:400"><b style="font-weight:600">Heading</b> Goes Here</div>
  <div class="t" style="left:25px;top:124px;width:332px;text-align:center">Clear advice helps owners plan growth, manage costs and lead their teams with confidence. Each plan starts with a frank look at where the business stands today, then sets priorities, owners and dates. Short reviews show what is working and what needs attention, so decisions rest on facts and every plan stays on track.</div>
  <div class="foot"><span class="fb"><i></i>Valmin &amp; Co</span><span class="fc">© Valmin &amp; Co 2023. All Rights Reserved.</span><span class="pg">14</span></div>
</div>

<div class="s" style="left:803px;top:1647px">
  <h2 class="hd"><b>Heading</b> Goes Here</h2>
  <div class="photo desk" style="left:24px;top:48px;width:102px;height:52px" role="img" aria-label="Photo of a man working on a tablet"></div>
  <div class="photo chart" style="left:140px;top:48px;width:102px;height:52px" role="img" aria-label="Photo of a pen over printed charts"></div>
  <div class="photo warm" style="left:256px;top:48px;width:102px;height:52px" role="img" aria-label="Photo of hands reviewing documents"></div>
  <div class="oh" style="left:24px;top:104px;width:102px;text-align:center">Heading <span>Goes Here</span></div>
  <div class="oh" style="left:140px;top:104px;width:102px;text-align:center">Heading <span>Goes Here</span></div>
  <div class="oh" style="left:256px;top:104px;width:102px;text-align:center">Heading <span>Goes Here</span></div>
  <div class="t" style="left:24px;top:114px;width:102px"><ul><li>Plan growth and manage costs with a clear view.</li><li>Set priorities and dates.</li><li>Review results each month and act early.</li></ul></div>
  <div class="t" style="left:140px;top:114px;width:102px"><ul><li>Plan growth and manage costs with a clear view.</li><li>Set priorities and dates.</li><li>Review results each month and act early.</li></ul></div>
  <div class="t" style="left:256px;top:114px;width:102px"><ul><li>Plan growth and manage costs with a clear view.</li><li>Set priorities and dates.</li><li>Review results each month and act early.</li></ul></div>
  <div class="foot"><span class="fb"><i></i>Valmin &amp; Co</span><span class="fc">© Valmin &amp; Co 2023. All Rights Reserved.</span><span class="pg">15</span></div>
</div>

<!-- row 6 -->
<div class="s" style="left:15px;top:1874px">
  <h2 class="hd"><b>Heading</b> Goes Here</h2>
  <div class="t" style="left:25px;top:52px;width:140px"><p>Clear advice helps owners plan growth, manage costs and lead teams with confidence. Each plan starts with a frank look at where the business stands today.</p><p>Short reviews show what works, what needs attention and where the next chance lies. Good reporting keeps everyone aligned, so decisions rest on facts rather than guesswork and every plan stays on track through change.</p></div>
  <svg style="position:absolute;left:170px;top:56px" width="80" height="80" viewBox="0 0 80 80"><circle cx="40" cy="40" r="33" fill="none" stroke="#eee" stroke-width="5"/><circle cx="40" cy="40" r="33" fill="none" stroke="var(--orange)" stroke-width="5" stroke-dasharray="132.7 207.3" transform="rotate(-90 40 40)"/><text x="40" y="46" text-anchor="middle" font-family="Poppins,sans-serif" font-weight="300" font-size="16" fill="var(--orange)">64%</text></svg>
  <svg style="position:absolute;left:262px;top:56px" width="80" height="80" viewBox="0 0 80 80"><circle cx="40" cy="40" r="33" fill="none" stroke="#eee" stroke-width="5"/><circle cx="40" cy="40" r="33" fill="none" stroke="var(--grey)" stroke-width="5" stroke-dasharray="170 207.3" transform="rotate(-90 40 40)"/><text x="40" y="46" text-anchor="middle" font-family="Poppins,sans-serif" font-weight="300" font-size="16" fill="var(--grey)">82%</text></svg>
  <div class="t" style="left:172px;top:142px;width:76px;text-align:center">Short note on this result for the owner to review.</div>
  <div class="t" style="left:264px;top:142px;width:76px;text-align:center">Short note on this result for the owner to review.</div>
  <div class="foot"><span class="fb"><i></i>Valmin &amp; Co</span><span class="fc">© Valmin &amp; Co 2023. All Rights Reserved.</span><span class="pg">16</span></div>
</div>

<div class="s" style="left:410px;top:1874px">
  <h2 class="hd"><b>Heading</b> Goes Here</h2>
  <svg style="position:absolute;left:26px;top:55px" width="180" height="120" viewBox="0 0 180 120" font-family="Poppins,sans-serif" font-size="3.5" fill="#555">
    <g stroke="#e5e5e5" stroke-width=".4"><path d="M12 100H175M12 85H175M12 70H175M12 55H175M12 40H175M12 25H175M12 10H175"/></g>
    <g text-anchor="end"><text x="9" y="101">0</text><text x="9" y="86">1</text><text x="9" y="71">2</text><text x="9" y="56">3</text><text x="9" y="41">4</text><text x="9" y="26">5</text><text x="9" y="11">6</text></g>
    <g><rect x="20" y="35.5" width="6" height="64.5" fill="var(--orange)"/><rect x="27" y="64" width="6" height="36" fill="var(--grey)"/><rect x="34" y="70" width="6" height="30" fill="#111"/>
       <rect x="60" y="62.5" width="6" height="37.5" fill="var(--orange)"/><rect x="67" y="34" width="6" height="66" fill="var(--grey)"/><rect x="74" y="70" width="6" height="30" fill="#111"/>
       <rect x="100" y="47.5" width="6" height="52.5" fill="var(--orange)"/><rect x="107" y="73" width="6" height="27" fill="var(--grey)"/><rect x="114" y="55" width="6" height="45" fill="#111"/>
       <rect x="140" y="32.5" width="6" height="67.5" fill="var(--orange)"/><rect x="147" y="58" width="6" height="42" fill="var(--grey)"/><rect x="154" y="25" width="6" height="75" fill="#111"/></g>
    <g text-anchor="middle"><text x="30" y="107">Category 1</text><text x="70" y="107">Category 2</text><text x="110" y="107">Category 3</text><text x="150" y="107">Category 4</text></g>
  </svg>
  <svg style="position:absolute;left:225px;top:60px" width="140" height="110" viewBox="0 0 140 110">
    <rect x="0" y="7" width="5" height="5" fill="var(--orange)"/><rect x="10" y="0" width="128" height="20" rx="3" fill="none" stroke="#ccc" stroke-width=".6"/>
    <rect x="0" y="45" width="5" height="5" fill="var(--grey)"/><rect x="10" y="38" width="128" height="20" rx="3" fill="none" stroke="#ccc" stroke-width=".6"/>
    <rect x="0" y="83" width="5" height="5" fill="#111"/><rect x="10" y="76" width="128" height="20" rx="3" fill="none" stroke="#ccc" stroke-width=".6"/>
  </svg>
  <div class="t" style="left:240px;top:64px;width:118px">Short note on this series and what it shows the owner.</div>
  <div class="t" style="left:240px;top:102px;width:118px">Short note on this series and what it shows the owner.</div>
  <div class="t" style="left:240px;top:140px;width:118px">Short note on this series and what it shows the owner.</div>
  <div class="foot"><span class="fb"><i></i>Valmin &amp; Co</span><span class="fc">© Valmin &amp; Co 2023. All Rights Reserved.</span><span class="pg">17</span></div>
</div>

<div class="s" style="left:803px;top:1874px">
  <h2 class="hd"><b>Heading</b> Goes Here</h2>
  <table class="grid">
    <tr><th>Heading</th><th class="hl">Column Title 1</th><th>Column Title 2</th><th>Column Title 3</th><th>Column Title 4</th></tr>
    <tr><td>Lorem ipsum dolor</td><td class="hl">Short cell note on this item here.</td><td>Short cell note on this item here.</td><td>Short cell note on this item here.</td><td>Short cell note on this item here.</td></tr>
    <tr><td>Lorem ipsum dolor</td><td class="hl">Short cell note on this item here.</td><td>Short cell note on this item here.</td><td>Short cell note on this item here.</td><td>Short cell note on this item here.</td></tr>
    <tr><td>Lorem ipsum dolor</td><td class="hl">Short cell note on this item here.</td><td>Short cell note on this item here.</td><td>Short cell note on this item here.</td><td>Short cell note on this item here.</td></tr>
    <tr><td>Lorem ipsum dolor</td><td class="hl">Short cell note on this item here.</td><td>Short cell note on this item here.</td><td>Short cell note on this item here.</td><td>Short cell note on this item here.</td></tr>
    <tr><td>Lorem ipsum dolor</td><td class="hl">Short cell note on this item here.</td><td>Short cell note on this item here.</td><td>Short cell note on this item here.</td><td>Short cell note on this item here.</td></tr>
  </table>
  <div class="foot"><span class="fb"><i></i>Valmin &amp; Co</span><span class="fc">© Valmin &amp; Co 2023. All Rights Reserved.</span><span class="pg">18</span></div>
</div>

<!-- row 7 -->
<div class="s" style="left:212px;top:2100px">
  <div class="photo night" style="inset:0" role="img" aria-label="Dim photo looking up at office towers"></div>
  <div class="brand on-dark" style="left:35px;top:42px"><div class="name"><i class="dot"></i>Valmin &amp; Co</div><div class="tag">Supporting Business Owners</div></div>
  <div class="ct on-dark" style="left:35px;top:112px">Contact Us</div>
  <div class="contact on-dark" style="left:35px;top:128px"><div><i></i>Phone Number Goes Here</div><div><i></i>E-Mail Address Goes Here</div><div><i></i>URL Address Goes Here</div></div>
  <div class="bar-bottom mist">© Valmin &amp; Co 2023. All Rights Reserved.</div>
</div>

<div class="s" style="left:606px;top:2100px">
  <div class="brand on-light" style="left:35px;top:42px"><div class="name"><i class="dot"></i>Valmin &amp; Co</div><div class="tag">Supporting Business Owners</div></div>
  <div class="ct" style="left:35px;top:112px;color:var(--orange)">Contact Us</div>
  <div class="contact on-light" style="left:35px;top:128px"><div><i></i>Phone Number Goes Here</div><div><i></i>E-Mail Address Goes Here</div><div><i></i>URL Address Goes Here</div></div>
  <div class="bar-bottom ink">© Valmin &amp; Co 2023. All Rights Reserved.</div>
</div>

</body>
</html>
```